SF Personal Styling Agency needs ad for Links Quarterly

We are a boutique personal styling and personal shopping agency based out of San Francisco, called Verity Wardrobe Advisory Group. We specialize in outfitting senior leaders in tech, helping them create images that endure and a personal styling with impact. People work with us so the world sees them as they want to be perceived. Our packages are listed on our site http://verity-advisory.example/ under services.

There are great reviews here: https://www.reviewhub.example/biz/verity-wardrobe-advisory-group-2

Our clientele is 60% female and 40% male. We need this ad to speak to both sexes. Our goal is to have people reach out to us and schedule consultations. The design should have a luxury feel and should have a design that is consistent with our website.

This ad is for a Links Quarterly. If people reach out to us and mention the Fairlook they get $100 off their first package. The attached add is what the Links Quarterly company came up with. It is a chintzy and too obvious - not what we want, but might be useful for dimension, phone number and email.

Target Market(s)

Men and women ages 36-65 in the greater San Francisco Bay area who are members of golf clubs and make upward of $150k/yr.

Industry/Entity Type

Shopping

Font styles to use
Sans Serif

Requirements
Must have
• Say - Mention "Fairlook" to get $100 off your first package
• Have phone number, website and email address
• Verity logo
• Be consistent with the look and feel of the website

```html
<!DOCTYPE html>
<html lang="en">
<head>
<meta charset="utf-8">
<title>Verity – Epic Style</title>
<link rel="stylesheet" href="https://fonts.googleapis.com/css2?family=Raleway:wght@200;300;400;500&family=Lato:ital,wght@0,300;0,400;1,300&display=swap">
<style>
  :root {
    --ink: #141414;
    --charcoal: #1d1d1b;
    --ivory: #f6f3e8;
    --gold: #c2b36a;
    --gold-soft: #d9cf9a;
    --mist: #a9a597;
    --white: #ffffff;
  }
  * { margin: 0; padding: 0; box-sizing: border-box; }
  html, body { width: 846px; height: 1200px; overflow: hidden; background: var(--white); }
  .ad {
    position: relative;
    width: 846px;
    height: 1200px;
    overflow: hidden;
    background: var(--charcoal);
    color: var(--ivory);
    font-family: "Lato", sans-serif;
  }

  /* Brand bar */
  .brand {
    position: absolute;
    left: 48px; top: 40px;
    display: flex; align-items: center; gap: 14px;
  }
  .brand__mark {
    width: 14px; height: 14px;
    background: var(--gold);
  }
  .brand__name {
    font-family: "Raleway", sans-serif;
    font-weight: 300;
    font-size: 26px;
    line-height: 30px;
    letter-spacing: 10px;
    color: var(--gold);
  }
  .tagline {
    position: absolute;
    right: 48px; top: 47px;
    font-family: "Raleway", sans-serif;
    font-weight: 400;
    font-size: 12px;
    line-height: 16px;
    letter-spacing: 4px;
    color: var(--mist);
    text-transform: uppercase;
  }
  .rule {
    position: absolute;
    left: 48px; width: 750px; height: 1px;
    background: var(--gold);
    opacity: 0.55;
  }
  .rule--top { top: 96px; }

  /* Headline */
  .headline {
    position: absolute;
    left: 48px; top: 128px;
    font-family: "Raleway", sans-serif;
    font-weight: 200;
    font-size: 80px;
    line-height: 84px;
    letter-spacing: 14px;
    color: var(--ivory);
  }
  .intro {
    position: absolute;
    left: 48px; top: 228px;
    width: 600px;
    font-family: "Lato", sans-serif;
    font-weight: 300;
    font-style: italic;
    font-size: 21px;
    line-height: 30px;
    color: var(--gold-soft);
  }

  /* Photography */
  .gallery {
    position: absolute;
    left: 48px; top: 312px;
    width: 750px; height: 480px;
    display: flex; gap: 15px;
  }
  .gallery__photo {
    flex: 1;
    border: 1px solid rgba(194,179,106,0.5);
  }
  .gallery__photo--coat {
    background: linear-gradient(to bottom, #5a4a3c 0%, #a8804f 30%, #9a6c3a 70%, #2a2724 100%);
  }
  .gallery__photo--dress {
    background: linear-gradient(to bottom, #4a3a34 0%, #8e2a2c 30%, #7a1e22 75%, #3a2f2c 100%);
  }
  .gallery__photo--jacket {
    background: linear-gradient(to bottom, #4c4038 0%, #2a3446 30%, #1f2838 75%, #2c2c28 100%);
  }

  /* Offer */
  .offer {
    position: absolute;
    left: 48px; top: 822px;
    width: 750px; height: 150px;
    border: 1px solid var(--gold);
    text-align: center;
    padding-top: 24px;
  }
  .offer__label {
    font-family: "Raleway", sans-serif;
    font-weight: 500;
    font-size: 12px;
    line-height: 16px;
    letter-spacing: 5px;
    color: var(--gold);
    text-transform: uppercase;
  }
  .offer__line {
    margin-top: 14px;
    font-family: "Raleway", sans-serif;
    font-weight: 300;
    font-size: 28px;
    line-height: 36px;
    color: var(--ivory);
  }
  .offer__line strong { font-weight: 500; color: var(--gold-soft); }
  .offer__note {
    margin-top: 12px;
    font-family: "Lato", sans-serif;
    font-weight: 300;
    font-size: 15px;
    line-height: 20px;
    letter-spacing: 1px;
    color: var(--mist);
  }

  /* Contact */
  .contact {
    position: absolute;
    left: 48px; top: 1000px;
    width: 750px;
    display: flex;
    justify-content: space-between;
    text-align: center;
  }
  .contact__item { width: 240px; }
  .contact__label {
    font-family: "Raleway", sans-serif;
    font-weight: 500;
    font-size: 11px;
    line-height: 14px;
    letter-spacing: 4px;
    color: var(--gold);
    text-transform: uppercase;
  }
  .contact__value {
    margin-top: 8px;
    font-family: "Lato", sans-serif;
    font-weight: 400;
    font-size: 17px;
    line-height: 22px;
    color: var(--ivory);
    white-space: nowrap;
  }
  .rule--bottom { top: 1070px; }

  /* Footer */
  .footer {
    position: absolute;
    left: 48px; top: 1092px;
    width: 750px;
    text-align: center;
  }
  .footer__packages {
    font-family: "Raleway", sans-serif;
    font-weight: 400;
    font-size: 15px;
    line-height: 20px;
    letter-spacing: 4px;
    color: var(--gold-soft);
    text-transform: uppercase;
  }
  .footer__area {
    margin-top: 12px;
    font-family: "Lato", sans-serif;
    font-weight: 300;
    font-size: 15px;
    line-height: 20px;
    color: var(--mist);
  }
  .footer__visit {
    margin-top: 8px;
    font-family: "Lato", sans-serif;
    font-weight: 300;
    font-size: 15px;
    line-height: 20px;
    color: var(--ivory);
    letter-spacing: 0.5px;
  }
</style>
</head>
<body>
<main class="ad">
  <div class="brand">
    <span class="brand__mark"></span>
    <span class="brand__name">VERITY</span>
  </div>
  <p class="tagline">Personal Styling &amp; Shopping</p>
  <div class="rule rule--top"></div>

  <h1 class="headline">EPIC STYLE</h1>
  <p class="intro">We help men and women develop a personal image with an enduring impression.</p>

  <div class="gallery">
    <div class="gallery__photo gallery__photo--coat" role="img" aria-label="Photo of a woman in a belted camel wool coat"></div>
    <div class="gallery__photo gallery__photo--dress" role="img" aria-label="Photo of a woman in a long red wrap dress"></div>
    <div class="gallery__photo gallery__photo--jacket" role="img" aria-label="Photo of a man in a navy pea coat over a striped sweater"></div>
  </div>

  <section class="offer">
    <p class="offer__label">Limited offer for our readers</p>
    <p class="offer__line">Mention “<strong>Fairlook</strong>” to get <strong>$100 off</strong> your first package</p>
    <p class="offer__note">Schedule your private consultation today</p>
  </section>

  <section class="contact">
    <div class="contact__item">
      <p class="contact__label">Call</p>
      <p class="contact__value">302-555-0147</p>
    </div>
    <div class="contact__item">
      <p class="contact__label">Visit</p>
      <p class="contact__value">verity-advisory.example</p>
    </div>
    <div class="contact__item">
      <p class="contact__label">Email</p>
      <p class="contact__value">hello@verity-advisory.example</p>
    </div>
  </section>
  <div class="rule rule--bottom"></div>

  <footer class="footer">
    <p class="footer__packages">Packages tailored to every style</p>
    <p class="footer__area">Personal shopping in the San Francisco Bay Area, Palo Alto and San Jose</p>
    <p class="footer__visit">1875 Harbor Lane, San Francisco, CA 94110</p>
  </footer>
</main>
</body>
</html>
```